Varnel Group Limited Stationary

We are in need of business card and letterhead designs. We are looking for clean modern designs that complement the style and feel of our logo.

```html
<!DOCTYPE html>
<html lang="en">
<head>
<meta charset="utf-8">
<title>Varnel Group Limited – Letterhead</title>
<link rel="stylesheet" href="https://fonts.googleapis.com/css2?family=Didact+Gothic&display=swap">
<style>
  :root {
    --backdrop: #ececec;
    --paper: #ffffff;
    --brand-blue: #1f4f8f;
    --ink-grey: #6b6b6b;
  }
  html, body {
    margin: 0;
    width: 1200px;
    height: 936px;
    overflow: hidden;
    background: var(--backdrop);
  }
  .letterhead {
    position: absolute;
    left: 297px;
    top: 46px;
    width: 606px;
    height: 844px;
    background: var(--paper);
    box-shadow: 0 2px 10px rgba(0,0,0,0.12);
    font-family: "Didact Gothic", sans-serif;
  }
  .brand {
    position: absolute;
    left: 62px;
    top: 70px;
    display: flex;
    align-items: center;
    gap: 10px;
  }
  .brand-dot {
    width: 24px;
    height: 24px;
    border-radius: 50%;
    background: var(--brand-blue);
  }
  .brand-name {
    font-family: "Didact Gothic", sans-serif;
    font-weight: 400;
    font-size: 19px;
    color: var(--brand-blue);
  }
  .contact-line {
    position: absolute;
    left: 30px;
    right: 30px;
    bottom: 22px;
    margin: 0;
    font-size: 9px;
    color: var(--ink-grey);
    white-space: nowrap;
    text-align: left;
  }
  .contact-line .label {
    color: var(--brand-blue);
  }
  .footer-band {
    position: absolute;
    left: 0;
    right: 0;
    bottom: 0;
    height: 14px;
    background: var(--brand-blue);
  }
</style>
</head>
<body>
  <main class="letterhead">
    <header class="brand">
      <span class="brand-dot"></span>
      <span class="brand-name">Varnel Group</span>
    </header>
    <footer>
      <p class="contact-line">
        Suite 4, 58 Calder Rd, Marlowe 4120 &nbsp;|&nbsp;
        <span class="label">T:</span> (07) 5550 1427 &nbsp;|&nbsp;
        <span class="label">F:</span> (07) 5550 1428 &nbsp;|&nbsp;
        <span class="label">E:</span> info@varnelgroup.com &nbsp;·&nbsp; www.varnelgroup.com
      </p>
      <div class="footer-band"></div>
    </footer>
  </main>
</body>
</html>
```